Real Estate Flyer

I would like an A4 size flyer which has the same info 3 times and can be cut into three.
It will be used for letterbox drops for new listings (SELLING) and sold listings (SOLD). The flyer needs a heading (as above) and a space for a photo which is able to be changed for each new property. Needs to be blue, red and white. It also requires my photo, KLT logo, Marisse Thornbury logo and the following text:
"Are you considering selling? Call Marisse today for a complimentary market appraisal".
(KLT logo, Marisse Thornbury Sales Consultant logo and my photo can be found in uploaded files)
Industry/Entity Type
Real Estate
Look and feel

```html
<!DOCTYPE html>
<html lang="en">
<head>
<meta charset="utf-8">
<title>Real Estate Flyer – Marisse Thornbury</title>
<link rel="stylesheet" href="https://fonts.googleapis.com/css2?family=Open+Sans:wght@400;600;700&family=Arimo:wght@700&display=swap">
<style>
  :root {
    --brand-blue: #1f7fc4;
    --deep-blue: #1d4f91;
    --sky-blue: #8fc6ec;
    --brand-red: #e8262b;
    --ink: #2b2b2b;
    --white: #ffffff;
    --page: #f2f2f2;
  }
  * { margin: 0; padding: 0; box-sizing: border-box; }
  html, body { width: 1168px; height: 1200px; overflow: hidden; background: var(--page); }
  body { font-family: "Open Sans", Arial, sans-serif; position: relative; }

  .flyer {
    position: absolute; left: 346px; top: 90px;
    width: 476px; height: 1020px;
    background: var(--white);
    box-shadow: 0 6px 18px rgba(0,0,0,.25);
    overflow: hidden;
  }
  .flyer > * { position: absolute; }

  .top-rule { left: 0; top: 30px; width: 476px; height: 8px; }

  .agency-badge { left: 240px; top: 12px; width: 220px; height: 78px; }
  .agency-name {
    left: 262px; top: 20px; width: 180px; height: 42px;
    display: flex; align-items: center; justify-content: center; gap: 10px;
    color: var(--white); font-weight: 700; font-size: 24px; letter-spacing: .5px;
  }
  .agency-name .mark { width: 14px; height: 14px; background: var(--white); }

  .property-photo {
    left: 0; top: 100px; width: 476px; height: 288px;
    background: linear-gradient(180deg, #cfe6f6 0%, #e9dcc0 45%, #c99a55 65%, #6f9a48 88%, #557f38 100%);
  }
  .photo-curve { left: 0; top: 100px; width: 476px; height: 288px; }
  .photo-rule { left: 0; top: 386px; width: 476px; height: 14px; }

  .status-tag {
    left: 22px; top: 66px; width: 176px; height: 70px;
    background: var(--brand-red); color: var(--white);
    border: 3px solid var(--white); border-radius: 10px;
    box-shadow: 2px 3px 6px rgba(0,0,0,.35);
    transform: rotate(-16deg);
    font-family: "Arimo", Arial, sans-serif; font-size: 38px; font-weight: 700;
    display: flex; align-items: center; justify-content: center;
  }

  .consultant-id { left: 18px; top: 416px; display: flex; align-items: center; gap: 14px; }
  .consultant-id .mark { width: 42px; height: 42px; background: var(--brand-red); }
  .consultant-name { font-size: 21px; font-weight: 400; color: var(--ink); line-height: 1.1; }
  .consultant-role { font-size: 11px; color: var(--ink); margin-left: 32px; }
  .consultant-phone { font-size: 11px; color: var(--brand-red); margin-left: 72px; }

  .headline-band { left: 0; top: 430px; width: 476px; height: 300px; }
  .headline {
    left: 0; top: 535px; width: 476px; text-align: center;
    color: var(--white); font-weight: 600; line-height: 1.15;
  }
  .headline .line-1 { display: block; font-size: 38px; letter-spacing: -1px; }
  .headline .line-2 { display: block; font-size: 46px; }

  .consultant-photo {
    left: 40px; top: 672px; width: 148px; height: 224px;
    background: linear-gradient(180deg, #d8d2c6 0%, #b9ab98 55%, #2a2a2e 100%);
  }

  .call-to-action {
    left: 220px; top: 740px; width: 240px; line-height: 1;
    font-weight: 700; text-transform: uppercase;
  }
  .call-to-action span { display: block; }
  .cta-call { font-size: 56px; color: var(--sky-blue); -webkit-text-stroke: 1.5px var(--brand-blue); letter-spacing: -1px; }
  .cta-name { font-size: 44px; color: var(--brand-red); -webkit-text-stroke: 1px #b01a1e; margin-top: 6px; }
  .cta-today { font-size: 34px; color: var(--sky-blue); -webkit-text-stroke: 1.2px var(--brand-blue); margin-top: 8px; }

  .appraisal {
    left: 0; top: 905px; width: 476px; text-align: center;
    font-size: 22px; font-weight: 600; color: var(--brand-blue); letter-spacing: -.5px;
    text-transform: uppercase;
  }

  .phone-band {
    left: 0; top: 950px; width: 476px; height: 70px;
    background: var(--brand-red); color: var(--white);
    font-family: "Arimo", Arial, sans-serif; font-weight: 700; font-size: 40px;
    display: flex; align-items: center; justify-content: center;
  }
</style>
</head>
<body>
  <main class="flyer">
    <svg class="top-rule" viewBox="0 0 476 8" preserveAspectRatio="none" aria-hidden="true">
      <rect x="0" y="0" width="476" height="3" fill="var(--brand-blue)"/>
      <rect x="0" y="5" width="476" height="2" fill="var(--sky-blue)"/>
    </svg>

    <svg class="agency-badge" viewBox="0 0 220 78" aria-hidden="true">
      <path d="M0 0 H220 V50 L110 78 L0 50 Z" fill="var(--deep-blue)"/>
      <rect x="22" y="8" width="176" height="42" fill="none" stroke="var(--white)" stroke-width="2"/>
    </svg>
    <div class="agency-name"><span class="mark"></span>KLT Realty</div>

    <div class="property-photo" role="img" aria-label="Photo of the property for sale: two-storey house with lawn and a for-sale sign"></div>
    <svg class="photo-curve" viewBox="0 0 476 288" preserveAspectRatio="none" aria-hidden="true">
      <path d="M0 0 H96 C30 80 40 220 150 288 H0 Z" fill="var(--white)" opacity=".85"/>
      <path d="M96 0 C30 80 40 220 150 288" fill="none" stroke="var(--sky-blue)" stroke-width="3"/>
    </svg>
    <svg class="photo-rule" viewBox="0 0 476 14" preserveAspectRatio="none" aria-hidden="true">
      <rect x="0" y="0" width="476" height="6" fill="var(--brand-blue)"/>
      <rect x="0" y="9" width="476" height="3" fill="var(--sky-blue)"/>
    </svg>

    <div class="status-tag">SELLING</div>

    <div class="consultant-id">
      <span class="mark"></span>
      <div>
        <div class="consultant-name">Marisse Thornbury</div>
        <div class="consultant-role">Sales Consultant</div>
        <div class="consultant-phone">0400 218 536</div>
      </div>
    </div>

    <svg class="headline-band" viewBox="0 0 476 300" preserveAspectRatio="none" aria-hidden="true">
      <polygon points="0,90 476,0 476,220 0,300" fill="var(--brand-blue)"/>
    </svg>
    <h1 class="headline">
      <span class="line-1">ARE YOU CONSIDERING</span>
      <span class="line-2">SELLING ?</span>
    </h1>

    <div class="consultant-photo" role="img" aria-label="Portrait photo of Marisse Thornbury, sales consultant"></div>

    <p class="call-to-action">
      <span class="cta-call">Call</span>
      <span class="cta-name">Marisse</span>
      <span class="cta-today">Today for</span>
    </p>
    <p class="appraisal">A Complimentary Market Appraisal</p>

    <div class="phone-band">0400 218 536</div>
  </main>
</body>
</html>
```